Tidewell Hypnotherapy 2017 DL Card Flyer

We would like a double sided DL Card Flyer design.

We are a professional Hypnotherapy Clinic looking for a fresh clean design.

Front of card is summary info and back of flyer is detailed text.

I have attached documents with text for the front (dl size hypno 1) and back (dl size hypno 2) of the card and an indicative style of layout.

There are logo files uploaded as well as one image file.

The colors we like are blue, white and yellow/gold.
Updates

please note: when using the 'bright steps bold change' image, please only use the top half of the image. The girl is not to be in the image, just the words and light bulb with the chalk underline. thanks.. Added Sunday, March 19, 2017

Industry/Entity Type

Health And Wellness

Requirements
Must have
• Note. I have misspelled the www.TidewellHypnotherapy.com.au (missing an 'o' in the attachments to the brief). My error. Please amend in your design submissions.

```html
<!DOCTYPE html>
<html lang="en">
<head>
<meta charset="utf-8">
<title>Tidewell Hypnotherapy – DL Card Flyer</title>
<link href="https://fonts.googleapis.com/css2?family=Open+Sans:wght@400;600;700&family=Oswald:wght@500;600&family=Lobster&display=swap" rel="stylesheet">
<style>
  :root{
    --navy:#1f2a6e;
    --navy-deep:#151b4c;
    --blue:#2c3c98;
    --blue-light:#3c4fb0;
    --grey:#8d909c;
    --paper:#ffffff;
    --stage:#dcdde0;
    --ink:#1b1f3d;
  }
  *{box-sizing:border-box;margin:0;padding:0}
  html,body{width:1200px;height:1200px;overflow:hidden;background:var(--stage)}
  body{position:relative;font-family:"Open Sans",sans-serif}
  .side-label{position:absolute;top:34px;width:485px;text-align:center;font:700 27px "Open Sans",sans-serif;color:#111}
  .side-label.front{left:91px}
  .side-label.back{left:626px}

  .card{position:absolute;top:83px;width:485px;height:1029px;overflow:hidden;box-shadow:0 6px 18px rgba(0,0,0,.25)}
  .card--front{left:91px}
  .card--back{left:626px}
  .card svg.layer{position:absolute;left:0;top:0;width:485px;height:1029px}
  .card .abs{position:absolute}

  /* front */
  .brand{left:0;top:0;width:485px;height:165px;display:flex;align-items:center;justify-content:center;gap:18px}
  .brand__dot{width:104px;height:104px;border-radius:50%;background:var(--navy);flex:none}
  .brand__name{color:var(--navy);font:700 34px/1.05 "Open Sans",sans-serif;letter-spacing:.5px}
  .brand__name span{display:block;font-size:19px;letter-spacing:4px}
  .chalkboard{left:0;top:118px;width:485px;height:350px;background:radial-gradient(ellipse at 50% 28%,#6c6a5a 0%,#3b3d3e 35%,#2a2c2e 100%)}
  .quote-box{left:41px;top:481px;width:402px;height:102px;border:1px solid rgba(255,255,255,.35);display:flex;align-items:center;justify-content:center;text-align:center}
  .quote-box p{font:400 28px/1.25 "Lobster",cursive;color:#fff;margin-top:8px}
  .quote-mark{left:212px;top:452px;width:60px;height:46px;background:var(--blue);text-align:center;font:400 78px/1 "Lobster",cursive;color:#9aa4d9}
  .pill{background:var(--paper);border-radius:20px;text-align:center;color:var(--ink);font:500 20px/35px "Oswald",sans-serif;box-shadow:0 6px 8px rgba(0,0,0,.3)}
  .programs-title{left:41px;top:602px;width:402px;font-size:21px}
  .program-list{left:109px;top:664px;list-style:none}
  .program-list li{display:flex;align-items:center;gap:9px;height:38px;color:#fff;font-size:16px}
  .program-list li::before{content:"";width:17px;height:17px;border-radius:50%;border:2px solid #c9cde6;flex:none}
  .phone-badge{left:209px;top:857px;width:56px;height:56px;border-radius:50%;background:var(--paper)}
  .phone-number{left:0;top:900px;width:485px;text-align:center;font:600 60px/1 "Oswald",sans-serif;color:var(--navy-deep);letter-spacing:-1px}
  .website{left:0;top:981px;width:485px;height:48px;line-height:48px;text-align:center;background:var(--navy-deep);color:#fff;font-size:14px;letter-spacing:.8px}

  /* back */
  .program{left:41px;width:402px}
  .program .pill{font-size:19.5px}
  .program p{color:#fff;font-size:12.2px;line-height:15.6px;text-align:justify;margin-top:22px}
  .program .sessions{color:#fff;font:700 17px/1 "Open Sans",sans-serif;margin-top:7px;text-align:left}
  .back-note{left:0;top:949px;width:485px;text-align:center;font-size:13px;line-height:17px;color:#222}
  .back-strip{left:0;top:1013px;width:485px;height:16px;background:var(--navy-deep)}
</style>
</head>
<body>
  <div class="side-label front">Front Side</div>
  <div class="side-label back">Back Side</div>

  <!-- FRONT -->
  <section class="card card--front">
    <svg class="layer" viewBox="0 0 485 1029" aria-hidden="true">
      <defs>
        <radialGradient id="blueGlowF" cx="50%" cy="40%" r="70%">
          <stop offset="0" stop-color="#3c4fb0"/><stop offset="1" stop-color="#222e7a"/>
        </radialGradient>
      </defs>
      <rect width="485" height="1029" fill="url(#blueGlowF)"/>
    </svg>
    <div class="abs chalkboard" role="img" aria-label="Chalkboard photo with the chalk words 'bright steps bold change' either side of a glowing light bulb, with chalk underlines"></div>
    <svg class="layer" viewBox="0 0 485 1029" aria-hidden="true">
      <defs>
        <linearGradient id="whiteF" x1="0" y1="0" x2="0" y2="1">
          <stop offset="0" stop-color="#fff"/><stop offset="1" stop-color="#e6e7ea"/>
        </linearGradient>
      </defs>
      <!-- header -->
      <path d="M0 150 C170 195 360 178 485 136 V148 C360 192 170 205 0 162 Z" fill="var(--grey)"/>
      <path d="M0 138 C170 186 360 168 485 128 V142 C360 184 170 198 0 152 Z" fill="var(--blue)"/>
      <path d="M0 0 H485 V128 C360 168 170 186 0 138 Z" fill="url(#whiteF)"/>
      <!-- photo lower edge -->
      <path d="M0 455 C150 405 330 395 485 462 V1029 H0 Z" fill="var(--grey)"/>
      <path d="M0 462 C150 412 330 402 485 469 V1029 H0 Z" fill="#fff"/>
      <path d="M0 472 C150 422 330 412 485 479 V880 H0 Z" fill="url(#blueGlowF)"/>
      <!-- footer -->
      <path d="M0 893 C150 865 330 858 485 885 V1029 H0 Z" fill="var(--blue-light)"/>
      <path d="M0 899 C150 872 330 865 485 892 V1029 H0 Z" fill="var(--grey)"/>
      <path d="M0 904 C150 878 330 871 485 898 V1029 H0 Z" fill="url(#whiteF)"/>
    </svg>

    <header class="abs brand">
      <div class="brand__dot"></div>
      <div class="brand__name">TIDEWELL<span>HYPNOTHERAPY</span></div>
    </header>

    <div class="abs quote-box"><p>“ There is nothing more<br>important than good health ”</p></div>
    <div class="abs quote-mark">“</div>

    <div class="abs pill programs-title">Professional Hypnosis Therapy Programs:</div>
    <ul class="abs program-list">
      <li>Weight Loss (Virtual Gastric Band)</li>
      <li>Sugar Addiction</li>
      <li>Quit Smoking</li>
      <li>Chronic Fatigue &amp; Chronic Pain Relief</li>
      <li>Stress Relief &amp; Deep Relaxation</li>
    </ul>

    <div class="abs phone-badge">
      <svg viewBox="0 0 56 56" width="56" height="56" aria-hidden="true">
        <path d="M15 22 Q28 12 41 22 L38 27 L34 25 L33 21 Q28 19 23 21 L22 25 L18 27 Z" fill="var(--navy-deep)"/>
        <path d="M19 29 H37 L40 42 H16 Z" fill="var(--navy-deep)"/>
        <g fill="#fff"><rect x="23" y="32" width="3" height="2"/><rect x="27" y="32" width="3" height="2"/><rect x="31" y="32" width="3" height="2"/><rect x="23" y="36" width="3" height="2"/><rect x="27" y="36" width="3" height="2"/><rect x="31" y="36" width="3" height="2"/></g>
        <path d="M40 12 q5 3 5 9 M43 9 q7 5 6 13" stroke="var(--navy-deep)" stroke-width="2" fill="none"/>
      </svg>
    </div>
    <div class="abs phone-number">1300 555 018</div>
    <div class="abs website">www.TidewellHypnotherapy.com.au</div>
  </section>

  <!-- BACK -->
  <section class="card card--back">
    <svg class="layer" viewBox="0 0 485 1029" aria-hidden="true">
      <defs>
        <radialGradient id="blueGlowB" cx="50%" cy="30%" r="75%">
          <stop offset="0" stop-color="#3c4fb0"/><stop offset="1" stop-color="#222e7a"/>
        </radialGradient>
        <linearGradient id="whiteB" x1="0" y1="0" x2="0" y2="1">
          <stop offset="0" stop-color="#fff"/><stop offset="1" stop-color="#e6e7ea"/>
        </linearGradient>
      </defs>
      <rect width="485" height="1029" fill="url(#blueGlowB)"/>
      <path d="M0 918 C150 890 330 883 485 910 V1029 H0 Z" fill="var(--grey)"/>
      <path d="M0 924 C150 897 330 890 485 917 V1029 H0 Z" fill="var(--blue-light)"/>
      <path d="M0 929 C150 903 330 896 485 923 V1029 H0 Z" fill="url(#whiteB)"/>
    </svg>

    <article class="abs program" style="top:42px">
      <h2 class="pill">WEIGHT LOSS PROGRAM (Virtual Gastric Band)</h2>
      <p>Achieve long term weight loss without dieting. Whether it’s losing 3kg or 30kg, we’ll help you become the shape and size you want to be. Our Internationally Accredited Program is proven to be 95% effective in clinical trials.</p>
      <p class="sessions">Number of Sessions: 6+</p>
    </article>

    <article class="abs program" style="top:210px">
      <h2 class="pill">SUGAR ADDICTION PROGRAM</h2>
      <p>Excess sugar intake can lead to obesity, Type 2 Diabetes and tooth decay. The habit of reaching for soft drinks, chocolate, sweets, cakes and biscuits can be hard to break. By rewiring your subconscious habits, our Program puts you back in control.</p>
      <p class="sessions">Number of Sessions: 3+</p>
    </article>

    <article class="abs program" style="top:380px">
      <h2 class="pill">QUIT SMOKING PROGRAM</h2>
      <p>The facts speak for themselves. You are 10 times more likely to quit smoking for good using hypnotherapy. Expect to be a non smoker after completing the first session of our Program. (12 Month Guarantee)</p>
      <p class="sessions">Number of Sessions: 2</p>
    </article>

    <article class="abs program" style="top:539px">
      <h2 class="pill" style="font-size:18px">CHRONIC FATIGUE &amp; CHRONIC PAIN RELIEF PROGRAM</h2>
      <p>Chronic Fatigue, Fibromyalgia and Chronic Musculoskeletal Pain are diseases of modern living. The symptoms of fatigue and pain are very real, however the cause is usually emotional, and is generally hidden beyond our conscious awareness. Our Program comprises Education and Hypnosis to help you regain your health, your self esteem, your friends and your life, all in a manageable timeframe.</p>
      <p class="sessions">Number of Sessions: 6+</p>
    </article>

    <article class="abs program" style="top:751px">
      <h2 class="pill">STRESS RELIEF &amp; DEEP RELAXATION PROGRAM</h2>
      <p>Our Program gently uncovers the true source of your stress, and helps you reconnect to a natural inner calm. We teach you self hypnosis so that you have the tools to continue your experience.</p>
      <p class="sessions">Number of Sessions: 3+</p>
    </article>

    <p class="abs back-note">All Programs include take home CD’s personally recorded by<br>our therapists, using advanced hypnotic techniques.</p>
    <div class="abs back-strip"></div>
  </section>
</body>
</html>
```